1 Page Bio, describing our Mission to buy multifamily properties in Colorado Springs.

I am uploading a sample of an associate who is doing a similar thing in Tampa Florida. I will also upload an attempt by my assistant to make the flyer and I will upload 3 pictures to use, along with another document that has text to add. I want to be able to edit the document pretty easily inside a google doc. thanks, I want it to look clean and professional.

```html
<!DOCTYPE html>
<html lang="en">
<head>
<meta charset="utf-8">
<title>Colorado Springs Multifamily – One Page Bio</title>
<link href="https://fonts.googleapis.com/css2?family=Open+Sans:wght@300;400;600;700&family=Exo+2:wght@600;700&display=swap" rel="stylesheet">
<style>
:root{
  --teal:#4a726d;
  --mission:#3f8a7b;
  --slate:#4b5662;
  --ink:#3b4047;
  --panel:#efeff0;
  --rule:#b9bdc1;
  --white:#ffffff;
}
*{margin:0;padding:0;box-sizing:border-box}
html,body{width:961px;height:1200px;overflow:hidden;background:var(--white)}
body{font-family:"Open Sans",Arial,sans-serif;color:var(--ink);position:relative}
.flyer{position:absolute;inset:0;width:961px;height:1200px;overflow:hidden;background:var(--white)}

/* hero */
.hero{position:absolute;left:0;top:0;width:961px;height:383px;
  background:linear-gradient(180deg,#f4f4f4 0%,#ececec 45%,#d4d4d4 62%,#8f8f8f 78%,#5b5b5b 100%)}
.hero-photo{position:absolute;inset:0}
.mission-tab{position:absolute;left:0;top:48px;width:35px;height:112px;background:var(--teal);
  border-radius:0 6px 6px 0;display:flex;align-items:center;justify-content:center}
.mission-tab span{transform:rotate(-90deg);white-space:nowrap;color:var(--white);
  font-family:"Exo 2",sans-serif;font-weight:700;font-size:18px}
.mission-text{position:absolute;left:67px;top:84px;color:var(--mission);font-size:24px;font-weight:400;line-height:27px}
.logo-spot{position:absolute;left:773px;top:-65px;width:210px;height:210px;border-radius:50%;
  border:3px solid var(--teal);background:var(--white)}
.logo-spot span{position:absolute;left:30px;top:78px;width:120px;text-align:center;font-size:14px;line-height:19px;color:var(--ink)}

.values-band{position:absolute;left:0;top:312px;width:961px;height:71px;background:var(--teal);color:var(--white);
  font-size:15px;line-height:19px}
.values-band .col{position:absolute;top:9px}
.values-band b{font-weight:700}
.values-band .divider{position:absolute;top:10px;width:1px;height:54px;background:#c9d6d4}

/* left panel */
.panel{position:absolute;left:36px;top:400px;width:345px;height:744px;background:var(--panel)}
.panel .block{position:absolute;left:22px;right:6px}
.panel h2{font-family:"Exo 2",sans-serif;font-weight:700;font-size:20px;color:var(--slate);letter-spacing:.3px;line-height:24px;white-space:nowrap}
.panel ul{list-style:none;font-size:12.8px;line-height:18.2px;color:var(--ink)}
.panel li{padding-left:8px;position:relative;white-space:nowrap}
.panel li::before{content:"•";position:absolute;left:0;font-size:10px}
.panel .rule{position:absolute;left:22px;width:303px;height:1px;background:var(--rule)}
.stage-tag{position:absolute;left:-5px;display:inline-flex;align-items:center;height:19px}
.stage-tag span{background:var(--teal);color:var(--white);font-size:17px;line-height:19px;padding:0 16px 0 2px;
  clip-path:polygon(0 0,100% 0,calc(100% - 4px) 100%,0 100%)}
.stage-tag i{display:block;width:4px;height:19px;background:var(--teal);margin-left:3px;transform:skewX(20deg)}
.strategy ul{position:absolute;left:0;line-height:17.5px}
.strategy li::before{color:var(--mission)}

/* right column */
.market{position:absolute;left:420px;top:399px;width:290px;font-size:14.6px;line-height:20px}
.market h3,.target h3{display:inline;font-weight:700;color:var(--mission);font-size:14.6px}
.market ul{list-style:none}
.market li{padding-left:10px;position:relative}
.market li::before{content:"•";position:absolute;left:0;color:var(--mission);font-size:10px}
.target{position:absolute;left:726px;top:399px;width:215px;font-size:14.6px;line-height:19px}

.team-title{position:absolute;left:420px;top:535px;font-family:"Exo 2",sans-serif;font-weight:700;font-size:20px;color:var(--slate)}
.group-tab{position:absolute;left:420px;height:19px;border-bottom:1px solid var(--teal);width:352px}
.group-tab span{display:inline-block;background:var(--teal);color:var(--white);font-size:16px;line-height:19px;padding:0 6px 0 4px;border-radius:5px 5px 0 0}
.member{position:absolute;left:424px;width:372px}
.member h4{font-family:"Exo 2",sans-serif;font-weight:700;font-size:13px;color:var(--mission);line-height:16px;height:17px}
.member.advisor h4{color:var(--slate);font-size:11.5px;height:15px}
.member ul{list-style:none}
.member li{position:relative;padding-left:8px}
.member li::before{content:"•";position:absolute;left:0;font-size:9px}
.member.principal ul{font-size:12px;line-height:18.2px}
.member.advisor ul{font-size:10.6px;line-height:16px}
.member.advisor.wide ul{line-height:14.6px}
.member.advisor li::before{color:var(--mission)}
.portrait{position:absolute;left:806px;width:100px;height:136px}

/* footer */
.partner{position:absolute;left:34px;top:1169px;font-size:17px;line-height:22px;color:var(--ink)}
.contact-bar{position:absolute;left:213px;top:1166px;width:716px;height:34px;background:var(--teal);color:var(--white);
  display:flex;align-items:center;padding-left:26px;font-size:15px;gap:14px;white-space:nowrap}
.contact-bar b{font-weight:700}
.contact-bar .item{display:flex;align-items:center;gap:6px}
</style>
</head>
<body>
<div class="flyer">

  <section class="hero">
    <div class="hero-photo" role="img" aria-label="Black and white skyline photograph of downtown Colorado Springs" style="background:linear-gradient(180deg,rgba(255,255,255,0) 55%,rgba(120,120,120,.35) 75%,rgba(70,70,70,.55) 100%)"></div>
    <div class="mission-tab"><span>Our Mission</span></div>
    <p class="mission-text">To create a family business by purchasing<br>Multifamily Residences, one at a time.</p>
    <div class="logo-spot"><span>Logo<br>to Come??</span></div>
  </section>

  <section class="values-band">
    <p class="col" style="left:60px;width:230px"><b>The Process</b> : Buy right, manage right, and finance right.</p>
    <div class="divider" style="left:304px"></div>
    <p class="col" style="left:330px;width:300px"><b>Values</b>: To provide a white glove experience to all residences with a clean, safe, and fun environment.</p>
    <div class="divider" style="left:661px"></div>
    <p class="col" style="left:678px;width:260px"><b>The Target</b> : B and C class assets located in Colorado Springs or nearby submarkets.</p>
  </section>

  <aside class="panel">
    <h2 class="block" style="top:29px">WHY MULTIFAMILY?</h2>
    <ul class="block" style="top:54px">
      <li>Earn Monthly Cashflow</li>
      <li>Huge Tax Benefits</li>
      <li>Passive Income</li>
      <li>Historically Stable Investment</li>
      <li>Economies of Scale</li>
      <li>Housing is an Enduring need</li>
    </ul>
    <div class="rule" style="top:171px"></div>
    <h2 class="block" style="top:184px;left:26px">WHY &nbsp;COLORADO SPRINGS?</h2>
    <ul class="block" style="top:210px;left:26px">
      <li>Strong Job Growth ??</li>
      <li>Robust Population Growth ??</li>
      <li>?? Population increase by 2030</li>
      <li>Low unemployment Rate ??</li>
      <li>Many large firms relocating to Colorado Springs</li>
    </ul>
    <div class="rule" style="top:309px"></div>
    <div class="block strategy" style="top:0;left:17px;height:744px">
      <h2 style="position:absolute;top:331px;left:-5px">INVESTMENT STRATEGY</h2>
      <div class="stage-tag" style="top:360px"><span>Acquire</span><i></i></div>
      <ul style="top:380px">
        <li>Purchase underperforming<br>apartment communities</li>
        <li>Mom and Pop characteristics</li>
        <li>Class B and C buildings</li>
        <li>20-50 units</li>
        <li>Deferred maintenance</li>
        <li>Value-add opportunity</li>
      </ul>
      <div class="stage-tag" style="top:510px"><span>Reposition</span><i></i></div>
      <ul style="top:529px">
        <li>Hire professional management team</li>
        <li>Stabilize the property</li>
        <li>Fill vacancies</li>
        <li>Implement RUBS</li>
        <li>Change fee structure</li>
        <li>Raise remaining rents</li>
      </ul>
      <div class="stage-tag" style="top:641px"><span>Refinance &amp; Proceeds</span><i></i></div>
      <ul style="top:661px">
        <li>Refinance the property and roll<br>proceeds into next</li>
        <li>Sell the property and cash out or roll<br>into the next property</li>
      </ul>
    </div>
  </aside>

  <section class="market">
    <h3>The Market:</h3> Colorado Springs
    <ul>
      <li>Projected job growth of nearly 50%</li>
      <li>Below average unemployment rates.</li>
      <li>bove-average incomes.</li>
      <li>Solid economy, military, aerospace, electronics industry, and tourism.</li>
    </ul>
  </section>
  <section class="target"><h3>TheTarget</h3>: B and C class assets located in Colorado Springs or nearby submarkets.</section>

  <h2 class="team-title">THE TEAM</h2>
  <div class="group-tab" style="top:567px"><span>Principals</span></div>

  <div class="member principal" style="top:595px">
    <h4>Ryan Calloway</h4>
    <ul>
      <li>Licensed Colorado Real Estate Agent 18 years.</li>
      <li>Broker-Owner of two Summit Realty Franchises 7 and 2 Years.</li>
      <li>Real Estate investing for 5 years.</li>
      <li>Member of Keystone Investor Academy.</li>
      <li>Married 24 years to Marla, parenting 10 children together.</li>
      <li style="line-height:16px">Appeared on Dan and Leo's Apartment Hour podcast<br>Episode 43 -$2M portfolio.</li>
    </ul>
  </div>
  <div class="member principal" style="top:757px">
    <h4>Glen Calloway</h4>
    <ul>
      <li>Retired Electrical Engineer.</li>
      <li>Active Real Estate Investor/Consultant.</li>
      <li>Net worth over $4M -15 Grandchildren.</li>
    </ul>
  </div>

  <div class="group-tab" style="top:838px"><span>Advisors</span></div>
  <div class="member advisor" style="top:864px">
    <h4>Warren Hale</h4>
    <ul>
      <li>General partner on 103 Apartments</li>
      <li>Acquiring 101 more apartments in Q1 -2020</li>
      <li>Flips 4-8 houses &nbsp;a year</li>
      <li>Active member in the Dan &amp; Leo Community</li>
      <li>Accountability coach</li>
    </ul>
  </div>
  <div class="member advisor wide" style="top:977px;width:300px">
    <h4>Neil Foss</h4>
    <ul>
      <li>Neil is the owner/operator of Ember Residential Group and Ember Residential Management</li>
      <li>He has been in the real estate business for 13 years and has created a portfolio of over 1000 units while growing Ember Management with team of 15 staff members.</li>
      <li>He has taught real estate for the past 6 years and has dozens of highly successful students. Neil uses his extensive real estate experience to teach his students the “real” side of real estate.</li>
    </ul>
  </div>

  <svg class="portrait" style="top:583px" viewBox="0 0 100 136" role="img" aria-label="Photo of the two principals standing outdoors">
    <defs><linearGradient id="pg1" x1="0" y1="0" x2="0" y2="1"><stop offset="0" stop-color="#7f8c5d"/><stop offset="1" stop-color="#5a5550"/></linearGradient></defs>
    <polygon points="0,0 99,0 99,91 0,128" fill="url(#pg1)"/>
    <line x1="0" y1="135" x2="99" y2="97" stroke="var(--slate)" stroke-width="3"/>
  </svg>
  <svg class="portrait" style="top:852px" viewBox="0 0 100 136" role="img" aria-label="Black and white headshot of the first advisor">
    <defs><linearGradient id="pg2" x1="0" y1="0" x2="0" y2="1"><stop offset="0" stop-color="#f2f2f2"/><stop offset="1" stop-color="#c9c9c9"/></linearGradient></defs>
    <polygon points="0,0 99,0 99,91 0,128" fill="url(#pg2)" stroke="#e2e2e2" stroke-width="1"/>
    <line x1="0" y1="135" x2="99" y2="97" stroke="var(--slate)" stroke-width="3"/>
  </svg>
  <svg class="portrait" style="top:1013px" viewBox="0 0 100 136" role="img" aria-label="Black and white headshot of the second advisor">
    <defs><linearGradient id="pg3" x1="0" y1="0" x2="0" y2="1"><stop offset="0" stop-color="#f4f4f4"/><stop offset="1" stop-color="#9a9a9a"/></linearGradient></defs>
    <polygon points="0,0 99,0 99,91 0,128" fill="url(#pg3)" stroke="#e2e2e2" stroke-width="1"/>
    <line x1="0" y1="135" x2="99" y2="97" stroke="var(--slate)" stroke-width="3"/>
  </svg>

  <p class="partner">Partner with us</p>
  <footer class="contact-bar">
    <span>Conatct us <b>Ryan &amp; Glen Calloway</b></span>
    <span class="item">
      <svg width="13" height="13" viewBox="0 0 24 24" aria-hidden="true"><path fill="#ffffff" d="M6.6 10.8a15.1 15.1 0 006.6 6.6l2.2-2.2a1 1 0 011-.25 11.4 11.4 0 003.6.57 1 1 0 011 1V20a1 1 0 01-1 1A17 17 0 013 4a1 1 0 011-1h3.5a1 1 0 011 1 11.4 11.4 0 00.57 3.6 1 1 0 01-.25 1z"/></svg>
      <b>719-555-0147</b>
    </span>
    <span class="item">
      <svg width="13" height="11" viewBox="0 0 24 20" aria-hidden="true"><rect x="1" y="2" width="22" height="16" rx="2" fill="#ffffff"/><path d="M2 3l10 8 10-8" fill="none" stroke="#4a726d" stroke-width="2"/></svg>
      <b>contact@callowayhomes.com</b>
    </span>
  </footer>
</div>
</body>
</html>
```